Employee Wellbeing Model Graphic Design

A visual/graphic representation of our Employee Wellbeing model.
Our model is a combination of the Ara Kōrero Ahi model of health and wellbeing and the wellbeing continuum.
We would like the visual to be on one page. The design should be modern and simple.
The powerpoint attached shows the information we are wanting to share with our employees about our wellbeing programme.

Target Market(s)

Our employees

Industry/Entity Type

Event Management

Font styles to use
Sans Serif
Other font styles liked:
• calibri light

Colors
00AB8E
00BBA5
67D7C9
C6EFE9
E9F9F6

```html
<!DOCTYPE html>
<html lang="en">
<head>
<meta charset="utf-8">
<title>Our Wellbeing Framework</title>
<link rel="stylesheet" href="https://fonts.googleapis.com/css2?family=Arimo:wght@400;700&display=swap">
<style>
  :root {
    --backdrop: #2e2e2e;
    --paper: #f1f1ec;
    --ink: #222123;
    --frame: #f2d6c9;
    --mental: #222448;
    --physical: #df3a41;
    --family: #f49fc6;
    --spiritual: #461649;
    --land: #1f5c52;
    --unwell: #6e2a2a;
    --struggling: #ee5228;
    --going-ok: #f7b917;
    --thriving: #1aab4b;
    --footer: #5a4a3a;
    --white: #ffffff;
  }
  * { margin: 0; padding: 0; box-sizing: border-box; }
  html, body { width: 1200px; height: 1200px; overflow: hidden; }
  body {
    background: var(--backdrop);
    font-family: "Arimo", Arial, sans-serif;
    color: var(--ink);
    position: relative;
  }
  .poster {
    position: absolute; left: 219px; top: 65px;
    width: 762px; height: 1069px;
    background: var(--paper);
    overflow: hidden;
  }
  .poster > * { position: absolute; }
  .title {
    left: 23px; top: 18px;
    font-size: 45px; font-weight: 700; letter-spacing: -0.5px;
    line-height: 1;
  }
  .title-rule { left: 577px; top: 50px; width: 161px; height: 3px; background: var(--ink); }

  .house-frame {
    left: 90px; top: 411px; width: 549px; height: 303px;
    border: 3px solid var(--frame);
    background: var(--frame);
  }
  .pillar {
    left: 96px; width: 538px; height: 55px;
    display: flex; align-items: center;
    color: var(--white);
  }
  .pillar svg { position: absolute; left: 92px; width: 38px; height: 38px; }
  .pillar-text { margin-left: 155px; white-space: nowrap; }
  .pillar-name { font-size: 18px; font-weight: 700; }
  .pillar-desc { font-size: 14px; font-weight: 400; }
  .mental { top: 417px; background: var(--mental); }
  .physical { top: 476px; background: var(--physical); }
  .family { top: 535px; background: var(--family); }
  .spiritual { top: 595px; background: var(--spiritual); }
  .land { top: 655px; background: var(--land); }

  .roof { left: 0; top: 0; width: 762px; height: 560px; }
  .pou-label {
    left: 315px; top: 140px; width: 100px; text-align: center;
    color: var(--white); font-size: 25px; font-weight: 700;
  }

  .model-bracket { left: 645px; top: 456px; width: 40px; height: 225px; }
  .model-name {
    left: 640px; top: 514px; width: 120px; height: 120px;
  }
  .model-name span {
    position: absolute; left: 50%; top: 50%;
    transform: translate(-50%, -50%) rotate(-90deg);
    white-space: nowrap; font-weight: 700; font-size: 24px; line-height: 1;
  }
  .model-name .line-one { margin-left: -10px; }
  .model-name .line-two { margin-left: 20px; }

  .continuum {
    left: 54px; top: 716px; width: 621px; height: 65px;
    background: var(--frame); padding: 5px 6px;
    display: flex;
  }
  .stage {
    flex: 1; display: flex; align-items: center; gap: 10px;
    color: var(--white); font-weight: 700; font-size: 16px;
    padding-left: 26px;
  }
  .stage svg { width: 32px; height: 32px; flex: none; }
  .unwell { background: var(--unwell); }
  .struggling { background: var(--struggling); padding-left: 20px; }
  .going-ok { background: var(--going-ok); padding-left: 16px; }
  .thriving { background: var(--thriving); padding-left: 26px; }

  .continuum-bracket { left: 95px; top: 794px; width: 535px; height: 30px; }
  .continuum-label {
    left: 210px; top: 800px; width: 320px; text-align: center;
    font-size: 25px; font-weight: 700; background: var(--paper);
  }

  .legend { font-size: 13px; line-height: 19px; }
  .legend li { list-style: none; position: relative; padding-left: 23px; margin-bottom: 9px; }
  .legend li::before {
    content: ""; position: absolute; left: 0; top: 1px; width: 13px; height: 19px;
    background: var(--swatch);
  }
  .legend-left { left: 29px; top: 855px; width: 300px; }
  .legend-right { left: 430px; top: 855px; width: 310px; }

  .footer {
    left: 0; top: 973px; width: 762px; height: 96px;
    background: var(--footer);
  }
  .footer-name {
    position: absolute; right: 22px; top: 14px;
    color: var(--white); font-weight: 700; font-size: 27px;
    letter-spacing: 4px; line-height: 33px; text-align: center;
  }
</style>
</head>
<body>
<main class="poster">
  <h1 class="title">Our Wellbeing Framework</h1>
  <div class="title-rule"></div>

  <div class="house-frame"></div>

  <div class="pillar mental">
    <svg viewBox="0 0 40 40" fill="none" stroke="#fff" stroke-width="1.6"><path d="M12 34v-6c-4-2-6-6-6-11 0-7 6-12 13-12s13 5 13 12c0 5-3 8-6 9v8M6 20l-2 4h3"/><circle cx="19" cy="16" r="6"/></svg>
    <p class="pillar-text"><span class="pillar-name">Taha Hinegaro - </span><span class="pillar-desc">Mental/Emotional Health</span></p>
  </div>
  <div class="pillar physical">
    <svg viewBox="0 0 40 40" fill="none" stroke="#fff" stroke-width="1.6"><circle cx="20" cy="6" r="4"/><path d="M13 24V15a3 3 0 0 1 3-3h8a3 3 0 0 1 3 3v9M16 16v21h3V26h2v11h3V16"/></svg>
    <p class="pillar-text"><span class="pillar-name">Tana Tinana - </span><span class="pillar-desc">Physical Health</span></p>
  </div>
  <div class="pillar family">
    <svg viewBox="0 0 40 40" fill="none" stroke="#fff" stroke-width="1.6"><circle cx="20" cy="20" r="8"/><path d="M20 15v10M15 20h10"/><circle cx="7" cy="7" r="3"/><circle cx="33" cy="7" r="3"/><circle cx="7" cy="31" r="3"/><circle cx="33" cy="31" r="3"/><path d="M2 15a5 5 0 0 1 10 0M28 15a5 5 0 0 1 10 0M2 39a5 5 0 0 1 10 0M28 39a5 5 0 0 1 10 0"/></svg>
    <p class="pillar-text"><span class="pillar-name">Taha Whanau - </span><span class="pillar-desc">Family/Community Health</span></p>
  </div>
  <div class="pillar spiritual">
    <svg viewBox="0 0 40 40" fill="none" stroke="#fff" stroke-width="1.6"><path d="M20 4c4 4 5 9 3 14M20 4c-4 4-5 9-3 14M6 14c5 0 10 4 11 9M34 14c-5 0-10 4-11 9M4 24c4 6 10 8 16 8s12-2 16-8"/><circle cx="20" cy="20" r="2.5"/><path d="M14 36h12"/></svg>
    <p class="pillar-text"><span class="pillar-name">Taha Wairua - </span><span class="pillar-desc">Spiritual Health</span></p>
  </div>
  <div class="pillar land">
    <svg viewBox="0 0 40 40" fill="none" stroke="#fff" stroke-width="1.6"><path d="M22 4c-2 8-6 14-14 20M22 4c0 10 4 18 12 24M22 4l-2 30M14 18l-8 14M30 20l6 8M18 26l-4 8"/></svg>
    <p class="pillar-text"><span class="pillar-name">Whenua - </span><span class="pillar-desc">Land/Roots</span></p>
  </div>

  <svg class="roof" viewBox="0 0 762 560" aria-hidden="true">
    <g fill="var(--ink)">
      <rect x="340" y="70" width="51" height="80" rx="20"/>
      <rect x="85" y="293" width="51" height="110" rx="20"/>
      <rect x="592" y="293" width="51" height="110" rx="20"/>
    </g>
    <path d="M68 432 L365 152 L663 432" fill="none" stroke="var(--ink)" stroke-width="60" stroke-linecap="round" stroke-linejoin="miter"/>
  </svg>
  <p class="pou-label">Pou</p>

  <svg class="model-bracket" viewBox="0 0 40 225" fill="none" stroke="var(--ink)" stroke-width="1.5">
    <circle cx="9" cy="5" r="4" fill="var(--ink)"/>
    <circle cx="9" cy="220" r="4" fill="var(--ink)"/>
    <path d="M9 5h18a4 4 0 0 1 4 4v102M31 135v76a4 4 0 0 1-4 4H9"/>
  </svg>
  <div class="model-name">
    <span class="line-one">Ara</span>
    <span class="line-two">Kōrero Ahi</span>
  </div>

  <div class="continuum">
    <div class="stage unwell">
      <svg viewBox="0 0 32 32" fill="none" stroke="#fff" stroke-width="1.5"><circle cx="16" cy="16" r="14"/><path d="M16 8v10"/><circle cx="16" cy="23" r="1.5"/></svg>Unwell
    </div>
    <div class="stage struggling">
      <svg viewBox="0 0 32 32" fill="none" stroke="#fff" stroke-width="1.5"><path d="M10 30v-5c-4-2-6-6-6-10C4 8 10 3 17 3s11 5 11 11c0 4-2 7-5 8v8M4 17l-2 4h3"/><path d="M18 8l-4 7h4l-3 7"/></svg>Struggling
    </div>
    <div class="stage going-ok">
      <svg viewBox="0 0 32 32" fill="none" stroke="#fff" stroke-width="1.5"><path d="M2 14h5v14H2zM7 15l5-7c1-3 4-2 4 1l-1 5h7c2 0 3 2 2 4l-3 8c0 1-1 2-3 2H7"/><circle cx="25" cy="8" r="5"/><path d="M22.5 8l2 2 3-3.5"/></svg>Going OK
    </div>
    <div class="stage thriving">
      <svg viewBox="0 0 32 32" fill="none" stroke="#fff" stroke-width="1.5"><path d="M16 13c-4-3-6-5-6-7a3 3 0 0 1 6-1 3 3 0 0 1 6 1c0 2-2 4-6 7z"/><circle cx="16" cy="19" r="3"/><path d="M4 14l3 10 5 4v3M28 14l-3 10-5 4v3M12 26l4-3 4 3"/></svg>Thriving
    </div>
  </div>

  <svg class="continuum-bracket" viewBox="0 0 535 30" fill="none" stroke="var(--ink)" stroke-width="1.5">
    <circle cx="6" cy="5" r="4" fill="var(--ink)"/>
    <circle cx="528" cy="5" r="4" fill="var(--ink)"/>
    <path d="M6 5v19a3 3 0 0 0 3 3h106M436 27h89a3 3 0 0 0 3-3V5"/>
  </svg>
  <h2 class="continuum-label">The Wellbeing Continuum</h2>

  <ul class="legend legend-left">
    <li style="--swatch: var(--unwell)">People who are mentally unwell and/or have a diagnosed mental illness</li>
    <li style="--swatch: var(--struggling)">People who don’t meet the criteria for a diagnosable mental illness, but who may be highly stressed or distressed</li>
  </ul>
  <ul class="legend legend-right">
    <li style="--swatch: var(--going-ok)">People who lack general mental wellbeing and a sense of being reasonably happy with life</li>
    <li style="--swatch: var(--thriving)">People who are experiencing optimal/positive mental health.</li>
  </ul>

  <footer class="footer">
    <p class="footer-name">KŌWHAI<br>EVENT HALLS</p>
  </footer>
</main>
</body>
</html>
```